PLN Info Brochure

We need a brochure design for a new not-for-profit organisation that is aimed at providing homeless people with a residence that also provides counselling and vocational training to assist them to find suitable employment at the end of the program.
PLEASE NOTE:
Brochure to be A4.
I know the brochure is quite long, it is really a booklet, but please note that it does not have to have a lot of work done on it, I just want it to look professional and the front cover and inside page to look good.
Also please leave about 2-3 pages at the end as I will be adding in some architect drawings.
Please add in a last page with Contact written at the bottom - we will fill that in later. So please ensure it is editable in PDF.
Thank you so much.
Cheers
Nadine
Training

```html
<!DOCTYPE html>
<html lang="en">
<head>
<meta charset="utf-8">
<title>PLN Info Brochure – Learning For Residents</title>
<link rel="stylesheet" href="https://fonts.googleapis.com/css2?family=Arimo:wght@400;700&display=swap">
<style>
  :root {
    --backdrop: #2b2b2b;
    --paper: #ffffff;
    --olive: #8e8f3c;
    --olive-light: #bdbb7e;
    --amber: #f7a823;
    --amber-soft: #fcd27a;
    --ink: #1f1f1f;
    --ink-list: #555555;
  }
  * { margin: 0; padding: 0; box-sizing: border-box; }
  html, body { width: 1200px; height: 900px; overflow: hidden; }
  body { background: var(--backdrop); font-family: "Arimo", Arial, sans-serif; position: relative; }

  .page {
    position: absolute; left: 344px; top: 80px;
    width: 547px; height: 773px;
    background: var(--paper); overflow: hidden;
  }
  .page-decor { position: absolute; inset: 0; }

  .brand {
    position: absolute; left: 49px; top: 86px;
    display: flex; align-items: center; gap: 8px;
  }
  .brand-dot { width: 46px; height: 46px; border-radius: 50%; background: var(--amber); }
  .brand-name { font-size: 28px; font-weight: 400; color: var(--amber); letter-spacing: 1px; }

  .section-title {
    position: absolute; left: 49px; top: 159px;
    font-size: 22px; font-weight: 700; color: var(--olive);
  }
  .section-intro {
    position: absolute; left: 49px; top: 189px; width: 450px;
    font-size: 11px; line-height: 16px; color: var(--ink);
  }

  .course-list {
    position: absolute; left: 57px; top: 245px; list-style: none;
  }
  .course-list li {
    position: relative; padding-left: 15px;
    font-size: 11px; font-weight: 700; color: var(--ink-list);
    height: 19.3px; line-height: 14px;
  }
  .course-list li::before {
    content: ""; position: absolute; left: 0; top: 3px;
    width: 8px; height: 8px; border-radius: 50%;
    background: radial-gradient(circle at 35% 35%, var(--amber-soft), var(--amber));
  }

  .photo { position: absolute; left: 290px; width: 188px; }
  .photo-garden { top: 242px; height: 123px; background: linear-gradient(160deg, #7b6a4e, #6e8c3a 55%, #5a4632); }
  .photo-care { top: 376px; height: 133px; background: linear-gradient(135deg, #e4e8ee, #c9b8a6 50%, #4e6f9a); }
  .photo-desk { top: 521px; height: 125px; background: linear-gradient(135deg, #3a2d22, #8a7458 50%, #2a211a); }
</style>
</head>
<body>
  <article class="page">
    <svg class="page-decor" width="547" height="773" viewBox="0 0 547 773" aria-hidden="true">
      <defs>
        <linearGradient id="band" x1="0" x2="1" y1="0" y2="0">
          <stop offset="0" stop-color="var(--olive)"/>
          <stop offset="0.55" stop-color="var(--olive-light)"/>
          <stop offset="1" stop-color="var(--olive)"/>
        </linearGradient>
      </defs>
      <!-- header band -->
      <rect x="0" y="0" width="547" height="140" fill="url(#band)"/>
      <path d="M0,52 C180,18 400,30 547,132 L547,140 L0,140 Z" fill="var(--paper)"/>
      <path d="M0,58 C180,22 400,34 547,132" fill="none" stroke="var(--amber)" stroke-width="5"/>
      <path d="M0,49 C180,14 400,26 547,126" fill="none" stroke="var(--paper)" stroke-width="3"/>
      <!-- footer band -->
      <path d="M0,722 C200,742 420,720 547,668 L547,773 L0,773 Z" fill="url(#band)"/>
      <path d="M0,730 C200,750 420,728 547,676" fill="none" stroke="var(--paper)" stroke-width="6"/>
      <path d="M0,724 C200,744 420,722 547,670" fill="none" stroke="var(--amber)" stroke-width="4"/>
      <g fill="var(--paper)" opacity="0.55">
        <rect x="330" y="735" width="5" height="38"/>
        <rect x="346" y="732" width="5" height="41"/>
        <rect x="362" y="728" width="5" height="45"/>
        <rect x="378" y="724" width="5" height="49"/>
        <rect x="394" y="720" width="5" height="53"/>
        <rect x="410" y="715" width="5" height="58"/>
        <rect x="426" y="710" width="5" height="63"/>
        <rect x="442" y="705" width="5" height="68"/>
        <rect x="458" y="699" width="5" height="74"/>
        <rect x="474" y="693" width="5" height="80"/>
        <rect x="490" y="687" width="5" height="86"/>
        <rect x="506" y="681" width="5" height="92"/>
        <rect x="522" y="686" width="5" height="87"/>
        <rect x="538" y="686" width="5" height="87"/>
      </g>
    </svg>

    <div class="brand">
      <span class="brand-dot"></span>
      <span class="brand-name">PLN</span>
    </div>

    <h1 class="section-title">Learning For Residents</h1>
    <p class="section-intro">Below is a summary of the types of vocational training that will be available for Residents. Case Workers will also assist the Residents to find work experience during the learning phase of their Program and employment upon completion of their Program.</p>

    <ul class="course-list">
      <li>Accounting &amp; Finance</li>
      <li>Administration</li>
      <li>Animal Care</li>
      <li>Beauty</li>
      <li>Business</li>
      <li>Community and Aged Care</li>
      <li>Counselling</li>
      <li>Design</li>
      <li>Editing &amp; Proofreading</li>
      <li>Education and Childcare</li>
      <li>Health</li>
      <li>Horticulture &amp; Gardening</li>
      <li>Human Resources</li>
      <li>Information Technology</li>
      <li>Journalism</li>
      <li>Management</li>
      <li>Mechanics</li>
      <li>Natural Therapies</li>
      <li>Photography</li>
      <li>Tourism &amp; Hospitality</li>
      <li>Writing &amp; Communication</li>
    </ul>

    <div class="photo photo-garden" role="img" aria-label="Photo of hands planting colourful flowers in pots with a watering can"></div>
    <div class="photo photo-care" role="img" aria-label="Photo of a young carer smiling with an elderly woman"></div>
    <div class="photo photo-desk" role="img" aria-label="Photo of a hotel receptionist on the phone at a front desk"></div>
  </article>
</body>
</html>
```